Car Repair Business Website Redesign

We need a new design for our wordpress website, which generates traffic and converts leads for our car repair business. The site was originally setup with a blank template and the design was never tweaked. All content is in place, so the design needs to arrange existing content into a visually strong, responsive layout with top priority given to conversion. You can view the existing website at www.brightlanegarageworks.com. Responsive design is extremely important - 36% of visitors are mobile and 18% tablet - so please include mobile designs.
To confirm, the brief is for PSD only, please supply designs for the following two pages:-
http://www.brightlanegarageworks.com/
http://www.brightlanegarageworks.com/clutch-replacement/
Target Market(s)
Predominantly male (75%), 25-55 year old (70%) audience.
Industry/Entity Type
Car Repair
Number of Pages Required
2 page
Font styles to use
Requirements
Must have
- Good use of colour, clear design elements. Our competitors just had a re-design which although not perfect, displays many good elements: www.gearvalet.com

```html
<!DOCTYPE html>
<html lang="en">
<head>
<meta charset="utf-8">
<title>Clutch Replacement – Brightlane Garage Works</title>
<link href="https://fonts.googleapis.com/css2?family=Montserrat:wght@400;500;600;700;800&family=Roboto:ital,wght@0,400;0,500;1,400&display=swap" rel="stylesheet">
<style>
:root{
  --blue:#0e6fb5;
  --blue-dark:#0b5c98;
  --ink:#1a1a1a;
  --text:#6a6a6a;
  --muted:#8a8a8a;
  --line:#dcdcdc;
  --star:#f07a22;
  --star-off:#555;
  --nav:#111;
}
*{box-sizing:border-box;margin:0;padding:0}
html,body{width:873px;height:1200px;overflow:hidden}
body{position:relative;background:#fff;font-family:'Roboto',sans-serif;color:var(--text);border-top:3px solid var(--blue)}
.abs{position:absolute}
a{color:var(--blue);text-decoration:none}

/* header */
.brand{left:94px;top:14px}
.brand-name{font-family:'Montserrat',sans-serif;font-weight:800;font-size:30px;color:var(--ink);letter-spacing:-1px;line-height:30px}
.brand-sub{font-family:'Montserrat',sans-serif;font-weight:500;font-size:7.5px;letter-spacing:2.6px;color:#333;margin-top:3px}
.social{right:94px;top:20px;display:flex;gap:6px}
.social span{width:16px;height:16px;background:var(--blue);display:block}
.call{right:94px;top:42px;font-family:'Montserrat',sans-serif;font-weight:500;font-size:14px;color:var(--ink)}
.call b{color:var(--blue);font-weight:600}

.nav{left:94px;top:73px;width:686px;height:27px;background:linear-gradient(#1e1e1e,#050505);display:flex}
.nav a{color:#fff;font-family:'Montserrat',sans-serif;font-size:9px;display:flex;align-items:center;justify-content:center;border-right:1px solid #3a3a3a;height:100%}
.nav a.active{background:var(--blue)}

/* left column */
.page-title{left:94px;top:118px;font-family:'Montserrat',sans-serif;font-weight:700;font-size:17.5px;color:var(--ink)}
.video{left:94px;top:154px;width:389px;height:235px;border:2px solid #333;background:#3c3c3c}
.video-scene{position:absolute;left:0;top:0;width:100%;height:200px;background:linear-gradient(#8a8d8a,#5d605d 70%,#4a4c4a)}
.play{position:absolute;left:152px;top:70px;width:82px;height:82px;border-radius:50%;background:rgba(50,50,50,.75)}
.controls{position:absolute;left:0;bottom:0;width:100%;height:31px;background:#1f1f1f;border-top:1px solid #555}
.intro{left:94px;top:402px;width:395px;font-size:9px;line-height:15px}
.intro p{margin-bottom:15px}

.box{border:1px solid #cfcfcf;box-shadow:0 1px 2px rgba(0,0,0,.08)}
.box-head-dark{background:#000;color:#fff;font-family:'Montserrat',sans-serif;font-weight:600;font-size:13px;padding:0 26px}
.why{left:94px;top:573px;width:389px;height:328px}
.why .box-head-dark{height:25px;line-height:25px}
.feature{height:76px;border-bottom:1px solid var(--line);position:relative;padding:10px 14px 0 59px}
.feature:last-child{border-bottom:0}
.feature h3{font-family:'Montserrat',sans-serif;font-weight:600;font-size:12px;color:#2a2a2a;margin-bottom:5px}
.feature p{font-size:7.6px;line-height:11.3px;color:var(--muted)}
.feature svg{position:absolute;left:14px;top:12px}

.steps{left:94px;top:914px;width:389px;height:247px}
.steps .box-head-dark{height:43px;padding-top:8px;line-height:15.5px}
.step{position:absolute;left:0;width:100%}
.step .num{position:absolute;left:25px;width:30px;height:30px;border:2px solid var(--blue);border-radius:50%;background:#fff;color:var(--blue);font-family:'Montserrat',sans-serif;font-weight:600;font-size:14px;text-align:center;line-height:26px}
.step h3{margin-left:70px;font-family:'Montserrat',sans-serif;font-weight:500;font-size:12px;color:#2a2a2a;margin-bottom:4px}
.step p{margin-left:70px;width:300px;font-size:8.6px;line-height:14px;color:#444}
.rail{position:absolute;left:39px;top:80px;width:3px;height:145px;background:#ccc}

/* right column */
.panel{left:518px;width:261px;background:#fff}
.panel-head{background:var(--blue);color:#fff;font-family:'Montserrat',sans-serif;font-weight:600;font-size:12.5px;height:28px;line-height:28px;padding-left:11px}
.quote{top:121px;height:161px}
.car{position:absolute;left:12px;top:53px;width:108px;height:82px;border-radius:30px 30px 10px 10px;background:#151515}
.off{position:absolute;left:136px;top:44px;font-family:'Montserrat',sans-serif;font-weight:700;font-size:24px;color:var(--blue)}
.btn{position:absolute;left:135px;top:83px;width:116px;height:28px;background:#000;border-radius:3px;color:#fff;font-family:'Montserrat',sans-serif;font-weight:600;font-size:11px;text-align:center;line-height:28px}
.note{position:absolute;left:137px;top:120px;font-family:'Montserrat',sans-serif;font-size:9.5px;color:#777;line-height:14px}
.note b{color:var(--blue);font-size:14px;font-weight:600}

.reviews{top:293px;height:266px}
.review{position:absolute;left:14px;width:238px}
.review .photo{position:absolute;left:0;top:0;width:48px;height:50px;border:1px solid #ddd;background:linear-gradient(#c7d6e3,#6d7f8f)}
.review .dark{background:linear-gradient(#888,#2a2a2a)}
.review h4{margin-left:64px;font-family:'Montserrat',sans-serif;font-weight:500;font-size:9px;color:#222;margin-top:4px}
.review .stars{position:absolute;right:0;top:0;font-size:11px;letter-spacing:1px;color:var(--star-off)}
.review .stars i{font-style:normal;color:var(--star)}
.review p{margin-left:64px;font-style:italic;font-size:8px;line-height:12.8px;color:#888;margin-top:3px}
.review a{display:block;margin-left:64px;margin-top:3px;font-size:8px;text-decoration:underline}

.list-item{border-bottom:1px solid #e2e2e2;padding:9px 12px 8px}
.list-item:last-child{border-bottom:0}
.list-item h3{font-family:'Montserrat',sans-serif;font-weight:600;font-size:10.5px;color:var(--blue);margin-bottom:4px}
.list-item p{font-size:8.3px;line-height:11.6px;color:#777}
.included{top:572px;height:266px}
.excluded{top:850px;height:310px}
.excluded .lead{font-family:'Montserrat',sans-serif;font-weight:500;font-size:10px;line-height:14px;color:#333;padding:9px 11px 6px}
.excluded .list-item p{line-height:13.6px}

.footer{left:0;top:1173px;width:873px;height:27px;background:var(--blue);color:#fff;font-size:8px}
.footer .copy{position:absolute;left:108px;top:9px}
.footer .links{position:absolute;right:104px;top:9px}
</style>
</head>
<body>

<header>
  <div class="abs brand">
    <div class="brand-name">brightlane</div>
    <div class="brand-sub">GARAGE WORKS</div>
  </div>
  <div class="abs social" aria-label="Social links"><span></span><span></span><span></span><span></span></div>
  <div class="abs call">Call Us Today : <b>0800 555 0142</b></div>
  <nav class="abs nav">
    <a style="width:55px">HOME</a>
    <a class="active" style="width:91px">SERVICES</a>
    <a style="width:100px">LOCATIONS</a>
    <a style="width:72px">FAQS</a>
    <a style="width:87px">ABOUT US</a>
  </nav>
</header>

<main>
  <h1 class="abs page-title">LOOKING FOR A CLUTCH REPLACEMENT</h1>

  <div class="abs video">
    <div class="video-scene" role="img" aria-label="Animated video still: a red car and a woman in a grey city street"></div>
    <div class="play"><svg width="82" height="82"><polygon points="33,24 33,58 60,41" fill="#fff"/></svg></div>
    <div class="controls">
      <svg width="385" height="31">
        <polygon points="11,10 11,20 19,15" fill="#fff"/>
        <rect x="24" y="14" width="236" height="4" fill="#444"/>
        <rect x="24" y="14" width="118" height="4" fill="#c8102e"/>
        <text x="220" y="20" font-family="Roboto" font-size="9" fill="#fff">0:00 <tspan fill="#888">/ 3:22</tspan></text>
        <polygon points="276,12 276,20 270,16" fill="#fff"/>
        <rect x="285" y="14" width="32" height="4" fill="#c8102e"/>
        <line x1="329" y1="0" x2="329" y2="31" stroke="#444"/>
        <rect x="339" y="11" width="12" height="9" fill="none" stroke="#fff" stroke-width="1.5"/>
        <text x="358" y="20" font-family="Roboto" font-style="italic" font-weight="500" font-size="11" fill="#fff">HD</text>
      </svg>
    </div>
  </div>

  <div class="abs intro">
    <p>We understand that finding a quality garage with the personal touch and that's good value for money can be a chore. But it shouldn't be – <a>that's exactly why Brightlane Garage Works exist.</a></p>
    <p>We're here to give you the bespoke service you deserve, because we understand that you need a helpful garage, transparent up front prices and a convenient service.</p>
    <p>Our quick and skilled mechanics will work hard to solve your clutch problems swiftly and painlessly – and all without the burden on your pocket.</p>
    <p>So why not get an instant online quote now, by entering your number plate?</p>
  </div>

  <section class="abs box why">
    <div class="box-head-dark">Why are we the best choice ?</div>
    <div class="feature">
      <svg width="30" height="44" viewBox="0 0 30 44"><polygon points="8,22 3,40 9,37 12,43 15,26" fill="var(--blue)"/><polygon points="22,22 27,40 21,37 18,43 15,26" fill="var(--blue)"/><circle cx="15" cy="14" r="13" fill="var(--blue)"/><circle cx="15" cy="14" r="9" fill="#fff"/><polygon points="15,8 17,12.5 21.5,12.8 18,15.8 19.2,20.3 15,17.8 10.8,20.3 12,15.8 8.5,12.8 13,12.5" fill="var(--blue)"/></svg>
      <h3>Quality</h3>
      <p>We only use genuine complete clutch kits from your vehicle OE manufacturer we never replace just part of the clutch either – so no need to worry about getting the job done again in a year's time</p>
    </div>
    <div class="feature" style="padding-left:60px">
      <svg width="32" height="38" viewBox="0 0 32 38"><path d="M16 1 L31 6 V17 C31 27 24 33 16 37 C8 33 1 27 1 17 V6 Z" fill="var(--blue)"/><path d="M16 5 L27 9 V17 H16 Z M16 17 H5 C6 25 10 30 16 33 Z" fill="#fff"/></svg>
      <h3>Reliability</h3>
      <p>We only use genuine complete clutch kits from your vehicle OE manufacturer we never replace just part of the clutch either – so no need to worry about getting the job done again in a year's time</p>
    </div>
    <div class="feature" style="padding-left:60px">
      <svg width="30" height="40" viewBox="0 0 30 40"><text x="0" y="36" font-family="Montserrat" font-weight="700" font-size="42" fill="var(--blue)">£</text></svg>
      <h3>Value</h3>
      <p>We only use genuine complete clutch kits from your vehicle OE manufacturer we never replace just part of the clutch either – so no need to worry about getting the job done again in a year's time</p>
    </div>
    <div class="feature" style="padding-left:60px">
      <svg width="32" height="40" viewBox="0 0 32 40"><circle cx="10" cy="4" r="3.5" fill="var(--blue)"/><path d="M10 10 V24 H22 L26 34" fill="none" stroke="var(--blue)" stroke-width="3.5" stroke-linejoin="round"/><path d="M6 18 A10 10 0 1 0 20 32" fill="none" stroke="var(--blue)" stroke-width="3"/></svg>
      <h3>Convenience</h3>
      <p>We only use genuine complete clutch kits from your vehicle OE manufacturer we never replace just part of the clutch either – so no need to worry about getting the job done again in a year's time</p>
    </div>
  </section>

  <section class="abs box steps">
    <div class="box-head-dark">Our Simple Three Step Solution Will Get You Back On The Road In No Time:</div>
    <div class="rail"></div>
    <div class="step" style="top:60px"><div class="num">1</div><h3>INSTANT ONLINE QUOTE</h3><p>It's easy – get your fully inclusive, fixed price clutch replacement quote instantly online or contact one our friendly team by giving us a call.</p></div>
    <div class="step" style="top:121px"><div class="num">2</div><h3>CALL US TO BOOK</h3><p>Call us to arrange a convenient date that works for you, and we'll collect your car in the morning and drop it back to you by the end of the day.</p></div>
    <div class="step" style="top:185px"><div class="num">3</div><h3>PAY ON COMPLETION</h3><p>You can arrange payment by debit or credit card once the work has been completed.</p></div>
  </section>

  <aside>
    <section class="abs box panel quote">
      <div class="panel-head">Your Instant Quote</div>
      <div class="car" role="img" aria-label="Black car front illustration"></div>
      <div class="off">10% OFF</div>
      <div class="btn">Get A Quote Now</div>
      <div class="note">AND RECIEVE YOUR<br><b>10%</b> DISCOUNT</div>
    </section>

    <section class="abs box panel reviews">
      <div class="panel-head">Our Latest Reviews</div>
      <div class="review" style="top:39px">
        <div class="photo" role="img" aria-label="Customer portrait photo"></div>
        <div class="stars"><i>★★★</i>★★</div>
        <h4>Tom Ashby</h4>
        <p>man arrived as agreed time very courteous offered some advice drove my car, left his, said tomorrow afternoon we</p>
        <a>Read More</a>
      </div>
      <div class="review" style="top:114px">
        <div class="photo dark" role="img" aria-label="Customer portrait photo"></div>
        <div class="stars"><i>★★</i>★★★</div>
        <h4>Karen Doyle</h4>
        <p>I was absolutely amassed at the fantastic service I received from the guys in the office and the mechanics that did a great job.</p>
        <a>Read More</a>
      </div>
      <div class="review" style="top:190px">
        <div class="photo dark" role="img" aria-label="Customer portrait photo"></div>
        <div class="stars"><i>★★★★</i>★</div>
        <h4>Sarah Linton</h4>
        <p>What a service!!! Called Tuesday, booked for a full clutch replacement, my car was picked up Thursday morning.</p>
        <a>Read More</a>
      </div>
    </section>

    <section class="abs box panel included">
      <div class="panel-head">What's Included</div>
      <div class="list-item"><h3>PARTS</h3><p>A full 3-piece clutch kit from your car's OE manufacturer. That includes either a clutch bearing or concentric slave cylinder.</p></div>
      <div class="list-item"><h3>LABOUR</h3><p>Every bit of work required to do the job – it's all included in the price.</p></div>
      <div class="list-item"><h3>COLLECTION AND DELIVERY</h3><p>Complimentary collection and drop off whenever is best for you.</p></div>
      <div class="list-item"><h3>2 YEAR WARRANTY</h3><p>That's parts and labour - all covered by a comprehensive 2 year warranty.</p></div>
    </section>

    <section class="abs box panel excluded">
      <div class="panel-head">What's Not Included</div>
      <div class="lead" style="border-bottom:1px solid #e2e2e2">WE VALUE HONESTY – SO HERE'S THE SMALL PRINT PLAIN AND SIMPLE.</div>
      <div class="list-item"><h3>DUAL MASS FLYWHEEL</h3><p>Not every vehicle is fitted with a Dual Mass Flywheel - if yours is, we'll give you a price along with your clutch quote. Around 1 in 3 need replacing, and we'll advise you on its condition while replacing your clutch.</p></div>
      <div class="list-item"><h3>RECOVERY</h3><p>If your car is undriveable and you don't have roadside assistance, we can arrange recovery for a small additional charge.</p></div>
      <div class="list-item"><h3>GEARBOX OIL</h3><p>Sometimes we might advise changing the gearbox oil too – but don't panic. We offer this for a fixed price of just £19 inc VAT.</p></div>
    </section>
  </aside>
</main>

<footer class="abs footer">
  <div class="copy">© 2015 BrightlaneGarageWorks.com All Right Reserved.</div>
  <div class="links">Terms &amp; Condition &nbsp;&nbsp;|&nbsp;&nbsp; Privacy Policy</div>
</footer>

</body>
</html>
```